Modify mobile web Photoshop design to make them look great

We need to choose and refine the stock image to look great on 5 mobile web pages: 1) Hourglass image on home screen, 2) Sofa image on registration screen, 3) Loveseat image on login screen, 4) Lamp for reminder screen, and 5) Bed for ratings / score screen. Sample photos denote what customer wants, but they are just downloaded from Brindo, and is not purchased stock photos. Designers need to show that the updated photos used are properly purchased from stock photo source. Photoshop files for all 5 mobile web pages are provided. Artists are requested to edit and submit the 5 photoshop files and make them look as good as possible with the constraints above. No change is needed on the layout or anything beside the 5 stock images, but subtle refinements are OK if you believe it would improve the overall design without affecting the art direction.

Target Market(s)

Travel, Lifestyle

Industry/Entity Type

Hospitality

Font styles to use
Sans Serif

Requirements
Must have
• Stock photos must be properly licensed, artists must put updated stock photos back into supplied photoshop source files, updated look and feel should have the same general art direction, images must be hourglass, sofa, loveseat, lamp and bed
Nice to have
• Minor and very subtle touchup of other elements without affecting any design work of the layout such as color scheme
Should not have
• Should not affect art direction, identity and color of all design and layout elements, should not use stock image other than the types specified (hourglass, sofa, loveseat, lamp and bed), should not use images not licensed from stock photo sites

```html
<!DOCTYPE html>
<html lang="en">
<head>
<meta charset="utf-8">
<title>dovel.co — Register</title>
<link rel="stylesheet" href="https://fonts.googleapis.com/css2?family=Open+Sans:wght@400;800&display=swap">
<style>
  :root {
    --ink: #111111;
    --text: #555555;
    --divider: #b9b9b9;
    --panel: rgba(244, 244, 244, 0.9);
    --field: #ffffff;
    --lavender: #b07fd6;
    --teal: #0e9591;
    --plum: #a3127c;
    --peach: #f2b482;
    --page: #ffffff;
    --frame: #222222;
  }
  * { box-sizing: border-box; margin: 0; padding: 0; }
  html, body { width: 676px; height: 1200px; overflow: hidden; background: var(--page); }
  body { font-family: "Open Sans", Arial, sans-serif; }

  .screen {
    position: relative;
    width: 676px;
    height: 1200px;
    border: 1px solid var(--frame);
    background: var(--page);
    overflow: hidden;
  }

  .top-bar .back { position: absolute; left: 36px; top: 28px; }
  .top-bar .menu { position: absolute; left: 602px; top: 38px; }
  .brand {
    position: absolute;
    left: 0; right: 0; top: 14px;
    text-align: center;
    font-weight: 800;
    font-size: 54px;
    letter-spacing: -2px;
    color: var(--ink);
  }

  .hero-photo {
    position: absolute;
    left: 0; top: 200px;
    width: 632px; height: 340px;
    border-radius: 22px 30px 4px 4px;
    background: linear-gradient(180deg, #5a5a5a 0%, #3a3a3a 38%, #bdbdbd 62%, #e6e6e6 100%);
  }

  .register-panel {
    position: absolute;
    left: 27px; top: 343px;
    width: 620px; height: 559px;
    background: var(--panel);
    border-radius: 8px;
  }

  .field {
    position: absolute;
    left: 54px;
    width: 508px;
    height: 48px;
    background: var(--field);
    border-bottom: 1px solid var(--accent);
    display: flex;
    align-items: center;
  }
  .field .icon {
    width: 56px;
    display: flex;
    justify-content: center;
    align-items: center;
    color: var(--accent);
    font-size: 15px;
  }
  .field .sep { width: 1px; height: 34px; background: var(--divider); }
  .field .value {
    padding-left: 12px;
    font-size: 18px;
    color: var(--text);
    flex: 1;
  }
  .field .trail { margin-right: 14px; display: flex; }

  .f-name  { top: 47px;  --accent: var(--lavender); }
  .f-id    { top: 118px; --accent: #555555; }
  .f-id .icon { color: var(--teal); }
  .f-dob   { top: 189px; --accent: var(--plum); }
  .f-dob .value { padding-left: 16px; }
  .f-id .value { padding-left: 16px; }
  .f-phone { top: 259px; --accent: var(--peach); }
  .f-pass  { top: 330px; --accent: var(--plum); }
  .f-pass .icon { color: var(--teal); }
  .f-email { top: 401px; --accent: var(--lavender); }

  .register-button {
    position: absolute;
    left: 55px; top: 476px;
    width: 506px; height: 47px;
    border: none;
    border-radius: 4px;
    background: var(--peach);
    color: #ffffff;
    font-family: inherit;
    font-size: 21px;
    letter-spacing: -0.5px;
  }

  .pager {
    position: absolute;
    top: 1090px; left: 267px;
    display: flex; gap: 13px;
  }
  .pager span { width: 20px; height: 20px; border-radius: 50%; }
</style>
</head>
<body>
<div class="screen">
  <header class="top-bar">
    <svg class="back" width="26" height="36" viewBox="0 0 26 36"><path d="M20 4 L6 18 L20 32" fill="none" stroke="#111" stroke-width="4.5"/></svg>
    <div class="brand">dovel.co</div>
    <svg class="menu" width="34" height="18" viewBox="0 0 34 18"><path d="M0 1H34M0 9H34M0 17H34" stroke="#111" stroke-width="2"/></svg>
  </header>

  <div class="hero-photo" role="img" aria-label="Photo of a grey tufted leather sofa on a white background"></div>

  <form class="register-panel">
    <div class="field f-name">
      <span class="icon"><svg width="24" height="28" viewBox="0 0 24 28"><circle cx="12" cy="9" r="6" fill="none" stroke="currentColor" stroke-width="1.4"/><path d="M2 27c0-6 4-10 10-10s10 4 10 10z" fill="none" stroke="currentColor" stroke-width="1.4"/></svg></span>
      <span class="sep"></span><span class="value">Full Name</span>
    </div>
    <div class="field f-id">
      <span class="icon"><svg width="32" height="22" viewBox="0 0 32 22"><rect x="1" y="1" width="30" height="20" rx="2" fill="none" stroke="currentColor" stroke-width="1.6"/><circle cx="10" cy="8" r="3" fill="none" stroke="currentColor" stroke-width="1.4"/><path d="M5 17c0-4 10-4 10 0z" fill="none" stroke="currentColor" stroke-width="1.4"/><path d="M19 7h8M19 11h8M19 15h8" stroke="currentColor" stroke-width="1.4"/></svg></span>
      <span class="sep"></span><span class="value">ID Number</span>
    </div>
    <div class="field f-dob">
      <span class="icon">DOB</span>
      <span class="sep"></span><span class="value">06/09/1980</span>
      <span class="trail"><svg width="26" height="28" viewBox="0 0 26 28"><rect x="1" y="4" width="24" height="23" rx="2" fill="var(--plum)"/><rect x="6" y="0" width="3" height="7" fill="var(--plum)"/><rect x="17" y="0" width="3" height="7" fill="var(--plum)"/><rect x="3" y="10" width="20" height="15" fill="#fff"/><g fill="var(--plum)"><rect x="5" y="12" width="4" height="3"/><rect x="11" y="12" width="4" height="3"/><rect x="17" y="12" width="4" height="3"/><rect x="5" y="17" width="4" height="3"/><rect x="11" y="17" width="4" height="3"/><rect x="17" y="17" width="4" height="3"/><rect x="5" y="21" width="4" height="3"/><rect x="11" y="21" width="4" height="3"/></g></svg></span>
    </div>
    <div class="field f-phone">
      <span class="icon"><svg width="20" height="32" viewBox="0 0 20 32"><rect x="1" y="1" width="18" height="30" rx="3" fill="var(--peach)" stroke="#e39a5f" stroke-width="1"/><rect x="4" y="5" width="12" height="20" fill="#f7c9a1"/><circle cx="10" cy="28" r="1.4" fill="#fff"/></svg></span>
      <span class="sep"></span><span class="value">Mobile Number</span>
    </div>
    <div class="field f-pass">
      <span class="icon"><svg width="26" height="26" viewBox="0 0 26 26"><circle cx="18" cy="8" r="7" fill="currentColor"/><circle cx="20" cy="6" r="2" fill="#fff"/><path d="M13 12 L2 23 L4 25 L6 23 L8 25 L10 23 L8 21 L16 14z" fill="currentColor"/></svg></span>
      <span class="sep"></span><span class="value">Set Password</span>
    </div>
    <div class="field f-email">
      <span class="icon"><svg width="24" height="16" viewBox="0 0 24 16"><rect width="24" height="16" fill="var(--lavender)"/><path d="M0 0 L12 9 L24 0 M0 16 L9 7 M24 16 L15 7" fill="none" stroke="#fff" stroke-width="1.3"/></svg></span>
      <span class="sep"></span><span class="value">Email</span>
    </div>
    <button class="register-button" type="button">REGISTER NOW</button>
  </form>

  <nav class="pager" aria-label="Steps">
    <span style="background: var(--lavender)"></span>
    <span style="background: var(--teal)"></span>
    <span style="background: var(--plum)"></span>
    <span style="background: var(--peach)"></span>
    <span style="background: var(--teal)"></span>
  </nav>
</div>
</body>
</html>
```